Painting Valtoni Renovations New buildings

Paint jobs plasterwork renovations new building customer painter paper drywall Entsorgungen.neukunden win color splash pleasure in colors competent clean fast reliable new try build demolition color combinations color concepts offers washing façade painting wood stains new projects old building renovations yes no beautiful new old sell secure solve paint over paint paint spray paint lye assemble disassemble sell buy trade oil dust new old assembly disassembly putty sanding fashion devastation copying belief feng shui kleopatra pompes beer colors swamp lime abrasion release tighten

Target Market(s)

construction industry

Contact Information for Business Card

Maler

Font styles to use
Serif

Colors
f04a50
959595

Requirements
Must have
• elegant appearance
Nice to have
• simply goal-oriented clientele in detail
Should not have
• too colorful

```html
<!DOCTYPE html>
<html lang="de">
<head>
<meta charset="utf-8">
<title>Valtoni – Visitenkarte</title>
<link rel="stylesheet" href="https://fonts.googleapis.com/css2?family=Nunito+Sans:wght@400;600;800;900&display=swap">
<style>
  :root {
    --navy: #1f3f82;
    --navy-deep: #19356f;
    --accent-red: #e8393f;
    --ink: #222428;
    --paper: #f7f7f7;
    --stage: #d9d9d9;
    --muted: #959595;
  }
  * { margin: 0; padding: 0; box-sizing: border-box; }
  html, body {
    width: 1200px; height: 1021px; overflow: hidden;
    background: var(--stage);
    font-family: "Nunito Sans", Arial, sans-serif;
  }
  .canvas {
    position: relative; width: 1200px; height: 1021px;
  }
  .card {
    position: absolute; left: 260px; width: 680px; height: 440px;
    box-shadow: 0 6px 18px rgba(0,0,0,.18);
  }
  .card--back { top: 47px; background: var(--navy); }
  .card--front { top: 534px; background: var(--paper); }

  .back-mark {
    position: absolute; left: 50%; top: 50%;
    transform: translate(-50%, -50%);
    display: flex; align-items: center; gap: 18px;
  }
  .back-mark__dot {
    width: 34px; height: 34px; border-radius: 50%; background: #fff;
  }
  .back-mark__name {
    color: #fff; font-weight: 900; font-size: 58px; letter-spacing: .5px;
  }

  .brand {
    position: absolute; left: 52px; top: 48px;
    display: flex; align-items: center; gap: 14px;
  }
  .brand__dot { width: 26px; height: 26px; border-radius: 50%; background: var(--navy); }
  .brand__name { color: var(--navy); font-weight: 900; font-size: 54px; line-height: 1; }

  .contact {
    position: absolute; left: 52px; top: 210px;
    font-size: 20px; line-height: 27px; color: var(--ink);
    list-style: none;
  }
  .contact li { display: flex; align-items: center; gap: 8px; }
  .contact .no-icon { padding-left: 26px; }
  .contact svg { width: 18px; height: 18px; flex: none; fill: none; stroke: var(--accent-red); stroke-width: 2; }

  .holder {
    position: absolute; left: 408px; top: 196px;
    color: var(--accent-red); font-weight: 800; font-size: 25px; letter-spacing: .3px;
  }
</style>
</head>
<body>
<main class="canvas">
  <section class="card card--back" aria-label="Rückseite">
    <div class="back-mark">
      <span class="back-mark__dot"></span>
      <span class="back-mark__name">Valtoni</span>
    </div>
  </section>

  <section class="card card--front" aria-label="Vorderseite">
    <div class="brand">
      <span class="brand__dot"></span>
      <span class="brand__name">Valtoni</span>
    </div>

    <ul class="contact">
      <li class="no-icon">Lindenweg 14</li>
      <li class="no-icon">8400 Musterdorf</li>
      <li>
        <svg viewBox="0 0 20 20"><path d="M5 2l3 4-2 2c1 2.5 3.5 5 6 6l2-2 4 3-2 3C9 18 2 11 2 4z" fill="#e8393f" stroke="none"/></svg>
        +41 00 123 45 67
      </li>
      <li>
        <svg viewBox="0 0 20 20"><rect x="2" y="4" width="16" height="12"/><path d="M2 4l8 7 8-7"/></svg>
        merenda@valtoni-maler.ch
      </li>
      <li>
        <svg viewBox="0 0 20 20"><circle cx="10" cy="10" r="8"/><ellipse cx="10" cy="10" rx="3.5" ry="8"/><path d="M2 10h16M4 5.5h12M4 14.5h12"/></svg>
        www.valtoni-maler.ch
      </li>
    </ul>

    <p class="holder">Merenda Valtoni</p>
  </section>
</main>
</body>
</html>
```